Canadian furniture distributor

I need a logo design for my new company, Pellham Craft G.P., Ergonomic High-End furniture distribution (very attractive patented design -mainly Desks & Chairs-).

Can be used for children adults, elders or limited mobility people.

Colors and design should match logo colors and products.

Industry/Entity Type

It Company

```html
<!DOCTYPE html>
<html lang="en">
<head>
<meta charset="utf-8">
<title>Pellham Craft G.P. — Business Card</title>
<link href="https://fonts.googleapis.com/css2?family=Poppins:wght@700&family=Questrial&display=swap" rel="stylesheet">
<style>
  :root {
    --backdrop: #e9e6e2;
    --card: #1c1c1d;
    --card-edge: #111112;
    --magenta: #9c2a5e;
    --gold: #f2b21f;
    --ink: #f4f4f4;
  }
  * { box-sizing: border-box; margin: 0; padding: 0; }
  html, body {
    width: 1200px; height: 716px; overflow: hidden;
    background: var(--backdrop);
  }
  .stage {
    position: relative; width: 1200px; height: 716px;
    display: flex; align-items: center; justify-content: center; gap: 60px;
  }
  .card {
    position: relative; width: 520px; height: 298px;
    background: var(--card);
    border: 1px solid var(--card-edge);
    box-shadow: 0 6px 18px rgba(0,0,0,.18);
  }
  /* Front */
  .card-front { display: flex; align-items: center; justify-content: center; gap: 14px; }
  .front-mark { width: 22px; height: 22px; background: var(--magenta); }
  .front-name {
    font-family: "Poppins", sans-serif; font-weight: 700;
    font-size: 30px; color: var(--gold); letter-spacing: -0.5px;
  }
  /* Back */
  .card-back { padding: 0; }
  .back-mark {
    position: absolute; left: 58px; top: 86px;
    width: 126px; height: 126px; background: var(--gold);
  }
  .back-details {
    position: absolute; right: 30px; top: 40px;
    text-align: right; font-family: "Questrial", sans-serif; color: var(--ink);
  }
  .company-name {
    font-family: "Poppins", sans-serif; font-weight: 700;
    font-size: 30px; line-height: 1; color: var(--magenta); letter-spacing: -0.5px;
  }
  .employee-name {
    margin-top: 14px; font-size: 13px; letter-spacing: .5px;
    color: var(--magenta); text-transform: uppercase;
  }
  .employee-title { font-size: 13px; margin-top: 2px; }
  .address { margin-top: 14px; font-size: 13px; line-height: 1.3; }
  .contacts { margin-top: 12px; list-style: none; font-size: 13px; line-height: 1.45; }
  .contacts li { display: flex; justify-content: flex-end; align-items: center; gap: 7px; }
  .icon { width: 12px; height: 12px; flex: none; }
  .icon-bg { fill: var(--gold); }
  .icon-ink { fill: none; stroke: var(--card); stroke-width: 1.3; stroke-linecap: round; }
</style>
</head>
<body>
<main class="stage">
  <section class="card card-front" aria-label="Card front">
    <span class="front-mark"></span>
    <span class="front-name">Pellham Craft G.P.</span>
  </section>

  <section class="card card-back" aria-label="Card back">
    <span class="back-mark"></span>
    <div class="back-details">
      <h1 class="company-name">Pellham Craft G.P.</h1>
      <p class="employee-name">Employee Name</p>
      <p class="employee-title">Title</p>
      <p class="address">48 Birchwood Lane Suite 210,<br>Ontario Canada K2P 1L4</p>
      <ul class="contacts">
        <li>613.555.0142
          <svg class="icon" viewBox="0 0 12 12"><rect class="icon-bg" width="12" height="12" rx="1"/><path class="icon-ink" d="M4 3c-1 1 0 4 2 5.5 1.5 1 2.5 1 3 .5"/></svg>
        </li>
        <li>613.555.0187
          <svg class="icon" viewBox="0 0 12 12"><rect class="icon-bg" width="12" height="12" rx="1"/><path class="icon-ink" d="M3.5 5h5v4h-5zM4.5 5V3h3v2"/></svg>
        </li>
        <li>hello@pellhamcraft.ca
          <svg class="icon" viewBox="0 0 12 12"><rect class="icon-bg" width="12" height="12" rx="1"/><path class="icon-ink" d="M2.5 3.5h7v5h-7zM2.5 3.5 6 6.5l3.5-3"/></svg>
        </li>
        <li>www.pellhamcraft.ca
          <svg class="icon" viewBox="0 0 12 12"><circle class="icon-bg" cx="6" cy="6" r="6"/><path class="icon-ink" d="M1 6h10M6 1c-2 3-2 7 0 10M6 1c2 3 2 7 0 10"/></svg>
        </li>
      </ul>
    </div>
  </section>
</main>
</body>
</html>
```